Wine Radio Show web re-design

We need new website look for an unconventional, nationally-syndicated WINE RADIO show. Show is fun, hip, witty and covers all wine lifestyle topics. We are redesigning logo and looking for a redesign of our wordpress site that hosts all our audio podcasts, and the site design needs to leverage and maximize these podcasts. Do NOT use the logo currently on the website. The site is corklantern.com, please see more info on the attached.

Do NOT use the logo currently on the website. Please just typeset the name "Cork Lantern Radio".
Updates

Please do NOT use the logo from the current website. Please just use type (to match theme/deisgn) "Cork Lantern Radio". Thank you.

Hello Designers, Thank you for working on this project. A piece of feedback overall is that we'd like much less image/masthead space in general (the photos and images at the top). We'd like the navigation and the latest Cork Lantern podcast to be above the fold. Most of the wine imagery/scenery shots can be minimalized/drastically reduced/eliminated, to allow more room for the different sections. Hope that makes sense, and again, thank you for working on this!! Marla

Target Market(s)

Wine lovers and wine industry professionals, probably 30+ years old

Industry/Entity Type

Radio

Font styles to use
Serif
Sans Serif
Decorative
Other font styles liked:
• Modern retro fonts

Requirements
Must have
• Must keep current content of site:
http://corklanternradio.com/podcast/
Feature podcasts prominently.
Do NOT use the logo currently on the website.
Nice to have
• Graphics to consider incorporating:
• WINE: Grapes, wine glasses, wine bottles, wine pouring, corkscrews, grapevines, vineyards
• RADIO symbols: soundwaves, antenna, radio icon, Podcast symbols, microphone
Should not have
• Do NOT use current logo - just use type.

```html
<!DOCTYPE html>
<html lang="en">
<head>
<meta charset="utf-8">
<title>Cork Lantern Radio</title>
<link rel="stylesheet" href="https://fonts.googleapis.com/css2?family=Open+Sans:wght@400;600;700&family=PT+Sans+Narrow:wght@700&family=Cormorant+SC:ital,wght@0,600;1,600&display=swap">
<style>
  :root {
    --wine: #9a0f2c;
    --wine-dark: #6e0a20;
    --player-red: #b0102e;
    --nav-dark: #2a1c17;
    --nav-line: #4a3a32;
    --gold: #e7b245;
    --cream: #efe9dd;
    --panel: #ffffff;
    --card-dark: #2b2b2b;
    --text: #6b6b6b;
    --text-dark: #333333;
    --orange: #d1741a;
    --signup: #efc981;
    --rule: #e2ddd3;
  }
  * { box-sizing: border-box; margin: 0; padding: 0; }
  html, body { width: 721px; height: 1200px; overflow: hidden; }
  body {
    background: var(--cream);
    font-family: "Open Sans", Arial, sans-serif;
    color: var(--text);
    position: relative;
  }
  .abs { position: absolute; }

  /* Masthead */
  .masthead {
    left: 0; top: 0; width: 721px; height: 269px;
    background:
      radial-gradient(ellipse at 50% 55%, #f4d57c 0%, #c99a3c 35%, #6f4a1c 75%, #3b2610 100%);
  }
  .brand {
    left: 258px; top: 0; width: 204px; height: 82px;
    background: var(--wine);
    border-radius: 0 0 18px 18px;
    display: flex; align-items: center; justify-content: center;
    text-align: center;
    color: #fff; font-weight: 700; font-size: 23px; line-height: 26px;
  }

  /* Navigation */
  .nav {
    left: 0; top: 269px; width: 721px; height: 32px;
    background: var(--nav-dark);
    border-bottom: 1px solid #120b08;
  }
  .nav ul {
    list-style: none; display: flex; position: absolute; left: 60px; top: 0; height: 32px;
    border-left: 1px solid var(--nav-line);
  }
  .nav li {
    height: 32px; padding: 0 9px; display: flex; align-items: center;
    color: #fff; font-size: 9.6px; border-right: 1px solid var(--nav-line);
  }
  .nav li.active { color: var(--gold); background: #3a2820; padding: 0 14px; }

  /* Player */
  .player {
    left: 59px; top: 314px; width: 602px; height: 29px;
    background: var(--player-red);
  }
  .player .dl { left: 16px; top: 9px; color: #ffd26a; font-size: 8.8px; font-weight: 600; }
  .player .track { left: 165px; top: 2px; width: 352px; height: 25px; background: #3a0810; }
  .player .time { color: #fff; font-size: 7px; line-height: 9px; top: 10px; }

  /* Main panel */
  .panel { left: 59px; top: 357px; width: 602px; height: 743px; background: var(--panel); }

  .section-title { color: var(--wine); font-size: 13.6px; font-weight: 600; }

  .card { left: 66px; width: 439px; border: 1px solid var(--rule); }
  .card-photo { left: 66px; width: 295px; height: 146px; }
  .card-info {
    left: 361px; width: 144px; height: 146px; background: var(--card-dark);
    padding: 12px 11px; color: #fff;
  }
  .card-info h3 {
    font-family: "PT Sans Narrow", "Arial Narrow", sans-serif; font-weight: 700;
    font-size: 13.6px; line-height: 17.6px; margin-bottom: 8px;
  }
  .card-info p { font-size: 7.8px; line-height: 15.4px; }
  .blurb { left: 76px; width: 420px; font-size: 7.8px; line-height: 13.8px; }
  .thumb { left: 75px; width: 82px; border: 1px solid var(--rule); padding: 3px; background: #fff; }
  .thumb .fill { width: 74px; }
  .thumb .caption { font-size: 5px; text-align: center; line-height: 7px; margin-top: 2px; color: #777; }
  .body-text { left: 166px; width: 330px; font-size: 7.8px; line-height: 13.8px; }
  .download-link { left: 166px; color: var(--wine); font-size: 9.6px; font-weight: 600; }

  .pager { left: 410px; top: 1068px; display: flex; align-items: center; gap: 5px; font-size: 8px; color: #888; }
  .pager .btn { width: 16px; height: 16px; border: 1px solid #ccc; border-radius: 50%; display: flex; align-items: center; justify-content: center; }

  /* Sidebar */
  .signup { left: 516px; top: 365px; width: 139px; height: 80px; background: var(--signup); padding: 7px 6px; }
  .signup h2 { color: var(--wine); font-size: 12.8px; font-weight: 600; margin-bottom: 6px; }
  .signup .field { background: #fff; height: 20px; font-size: 6.8px; padding: 6px 5px; color: #888; }
  .signup .go { position: absolute; right: 6px; top: 54px; background: var(--card-dark); color: #fff; font-size: 7.6px; padding: 3px 6px; }

  .recent-title { left: 516px; top: 458px; color: var(--wine); font-size: 12.8px; font-weight: 600; }
  .recent { left: 516px; width: 139px; border-bottom: 1px solid var(--rule); padding: 0 0 10px 10px; font-size: 7.8px; line-height: 11.2px; color: var(--text-dark); }
  .recent::before { content: ""; position: absolute; left: 2px; top: 3px; border-left: 4px solid #777; border-top: 3px solid transparent; border-bottom: 3px solid transparent; }
  .recent span { color: var(--orange); }
  .recent .date { display: block; margin-top: 5px; color: var(--orange); }

  .podstream { left: 516px; top: 696px; width: 139px; height: 44px; background: linear-gradient(#3a3a3a, #1f1f1f); color: #fff; font-size: 11px; line-height: 13px; padding: 8px 0 0 44px; }
  .podstream .icon { position: absolute; left: 9px; top: 8px; width: 28px; height: 28px; background: #1f6fd0; border-radius: 3px; }

  .book { left: 541px; top: 751px; width: 90px; height: 182px; background: #f3d98f; border: 1px solid #d9c08a; text-align: center; font-family: "Cormorant SC", Georgia, serif; color: #4a2a1a; }
  .book .lead { font-style: italic; font-size: 10px; margin-top: 4px; }
  .book .title { font-size: 9px; line-height: 10px; margin-top: 4px; }
  .book .cover { width: 72px; height: 100px; margin: 6px auto 0; background: linear-gradient(160deg, #7a2a3a, #5a1a28); }
  .book .cta { font-size: 9px; margin-top: 6px; }

  /* Footer */
  .footer-nav { left: 0; top: 1118px; width: 721px; display: flex; justify-content: center; font-size: 8px; color: #666; }
  .footer-nav span { padding: 0 9px; border-right: 1px solid #bbb; }
  .footer-nav span:last-child { border-right: 0; }
  .copyright { left: 0; top: 1137px; width: 721px; text-align: center; font-size: 8px; color: #666; }
  .social { left: 321px; top: 1160px; display: flex; gap: 5px; }
  .social i { width: 16px; height: 16px; border-radius: 50%; background: #9a9186; display: block; }
</style>
</head>
<body>

<header>
  <div class="abs masthead" role="img" aria-label="Golden vineyard sunset with wine barrels, bottles, glasses and grapes framed by curtains"></div>
  <div class="abs brand">Cork Lantern<br>Radio</div>
  <nav class="abs nav">
    <ul>
      <li class="active">Home</li><li>Episode Archives</li><li>Uncorked</li><li>About the Show</li><li>About the Host</li><li>On the Air</li><li>Blog</li><li>Store</li><li>Contact Us</li>
    </ul>
  </nav>
</header>

<div class="abs player">
  <div class="abs dl">DOWNLOAD THIS EPISODE</div>
  <svg class="abs" style="left:140px;top:5px" width="19" height="19" viewBox="0 0 19 19"><circle cx="9.5" cy="9.5" r="8.5" fill="#2a0a10" stroke="#fff" stroke-width="1.2"/><path d="M7.5 5.5 L13 9.5 L7.5 13.5Z" fill="#fff"/></svg>
  <div class="abs track"></div>
  <div class="abs time" style="left:169px">00:00</div>
  <svg class="abs" style="left:193px;top:9px" width="294" height="10"><rect x="0" y="2" width="294" height="5" rx="2.5" fill="#fff"/><rect x="0" y="2" width="117" height="5" rx="2.5" fill="#e01a2e"/><rect x="117" y="2" width="55" height="5" fill="#aaa"/><circle cx="117" cy="4.5" r="4.5" fill="#fff" stroke="#555"/></svg>
  <div class="abs time" style="left:494px">04:25</div>
  <svg class="abs" style="left:526px;top:8px" width="62" height="13"><path d="M1 4h3l4-3v11l-4-3H1z" fill="#fff"/><path d="M10 3q3 3.5 0 7M12.5 1q5 5.5 0 11" stroke="#fff" fill="none" stroke-width="1.2"/><rect x="20" y="5" width="41" height="3" rx="1.5" fill="#fff"/><rect x="20" y="5" width="27" height="3" fill="#2a0a10"/><rect x="46" y="1" width="3" height="11" fill="#fff"/></svg>
</div>

<main>
  <div class="abs panel"></div>

  <h2 class="abs section-title" style="left:68px;top:370px">This week on Cork Lantern :</h2>
  <div class="abs card" style="top:399px;height:305px"></div>
  <div class="abs card-photo" style="top:399px;background:linear-gradient(90deg,#8a5a38,#b07a4a 60%,#6e4428)" role="img" aria-label="Guest portrait in front of a wooden wine crate tied with a red ribbon"></div>
  <div class="abs card-info" style="top:399px">
    <h3>Episode #253 – Knowing Wine From Chen: The Expert Storyteller at Vinecellar.com</h3>
    <p>Posted by Cork Lantern<br>May 31, 2014<br>Episode Archives</p>
  </div>
  <p class="abs blurb" style="top:557px">This week on Cork Lantern Radio, one of America's foremost experts on the topic of all things Vino joins host Daniel Whitford for an in-depth discussion on the nation's favorite adult beverage.</p>
  <div class="abs thumb" style="top:593px">
    <div class="fill" style="height:72px;background:linear-gradient(#c7452a,#8a2a1c)" role="img" aria-label="Portrait of guest Walter Chen"></div>
    <div class="caption">Vinecellar.com Chief Storyteller<br>Walter Chen</div>
  </div>
  <p class="abs body-text" style="top:591px">Walter Chen started his career in a family-run wine shop and eventually pursued an opportunity with West Coast retailer CaskMart, where he ultimately served as the company's cellar master. Now, he is the Chief Storyteller on all-things-wine at national online retail giant Vinecellar.com. From the fascinating stories behind his career growth and celebrity reputation as a judge and advocate, to his take on what's hot and what's losing its luster with consumers, this is an episode every wine lover must hear.</p>
  <a class="abs download-link" style="top:677px">Download this Episode</a>

  <h2 class="abs section-title" style="left:68px;top:721px">Most Recent Episodes :</h2>
  <div class="abs card" style="top:750px;height:305px"></div>
  <div class="abs card-photo" style="top:750px;background:linear-gradient(90deg,#2a221c,#5a4a3a 55%,#3a2e24)" role="img" aria-label="Glass of red wine with a bottle and a wedge of cheese on a board"></div>
  <div class="abs card-info" style="top:750px">
    <h3>Episode #253 – Knowing Wine From Chen: The Expert Storyteller at Vinecellar.com</h3>
    <p>Posted by Cork Lantern<br>May 31, 2014<br>Episode Archives</p>
  </div>
  <p class="abs blurb" style="top:908px">This week on Cork Lantern Radio, one of America's foremost experts on the topic of all things Vino joins host Daniel Whitford for an in-depth discussion on the nation's favorite adult beverage.</p>
  <div class="abs" style="left:75px;top:944px;width:82px;height:98px;background:linear-gradient(#e8d9a8,#8a7a3a 60%,#4a3a20);border-radius:3px" role="img" aria-label="Wine bottle and glass on a barrel overlooking a vineyard"></div>
  <p class="abs body-text" style="top:942px">Walter Chen started his career in a family-run wine shop and eventually pursued an opportunity with West Coast retailer CaskMart, where he ultimately served as the company's cellar master. Now, he is the Chief Storyteller on all-things-wine at national online retail giant Vinecellar.com. From the fascinating stories behind his career growth and celebrity reputation as a judge and advocate, to his take on what's hot and what's losing its luster with consumers, this is an episode every wine lover must hear.</p>
  <a class="abs download-link" style="top:1028px">Download this Episode</a>

  <div class="abs pager">
    <span>Previous</span>
    <span class="btn"><svg width="6" height="6"><path d="M5 0 L0 3 L5 6Z" fill="#333"/></svg></span>
    <span class="btn"><svg width="6" height="6"><path d="M1 0 L6 3 L1 6Z" fill="#333"/></svg></span>
    <span>Next</span>
  </div>
</main>

<aside>
  <div class="abs signup">
    <h2>Newsletter Signup</h2>
    <div class="field">Enter your E-mail ID</div>
    <div class="go">Subscribe</div>
  </div>
  <h2 class="abs recent-title">Recent Shows</h2>
  <div class="abs recent" style="top:484px">Episode #253 – <span>Knowing Wine From Chen: The Expert Storyteller at Vinecellar.com</span><span class="date">May 31, 2014</span></div>
  <div class="abs recent" style="top:557px">Episode #253 – <span>Knowing Wine From Chen: The Expert Storyteller at Vinecellar.com</span><span class="date">May 31, 2014</span></div>
  <div class="abs recent" style="top:630px">Episode #253 – <span>Knowing Wine From Chen: The Expert Storyteller at Vinecellar.com</span><span class="date">May 31, 2014</span></div>
  <div class="abs podstream"><span class="icon"></span>Subscribe in<br>PodStream</div>
  <div class="abs book">
    <div class="lead">Just Released!</div>
    <div class="title">The New 2013<br>Central Coast<br>Second Edition</div>
    <div class="cover" role="img" aria-label="Guidebook cover with a vineyard landscape"></div>
    <div class="cta">Get Yours Here!</div>
  </div>
</aside>

<footer>
  <div class="abs footer-nav"><span>Home</span><span>Episode Archives</span><span>Uncorked</span><span>About the Show</span><span>About the Host</span><span>On the Air</span><span>Blog</span><span>Store</span><span>Contact Us</span></div>
  <div class="abs copyright">Copyright © 2014 Cork Lantern Radio. &nbsp;All rights reserved.</div>
  <div class="abs social"><i></i><i></i><i></i><i></i></div>
</footer>

</body>
</html>
```